Open House Real Estate Flyer

Looking for someone with a quick turn around to create an open house flyer for "P&W Realty Service; LLC.

Please include the attached pictures if possible and all information below.

Property Features:
8 Room, 2.5 Bath Colonial style home
Open concept, Kitchen, Dining room and Living room.
Deck
2 Car Garage

An example of how open house flyers look are below please use for informational purposes only.

Attached are the colors I would like to use for P&W Realty services flyer with my business card.

Date of event: Saturday, July 18, 2020
Time of event 12-3
Location 48 Orchard Ln Hamden, CT
Listing price 249,999

P&W Realty Services, LLC
Marta Quinlan
203 555-0187
FB: P&W Realty Service, LLC

```html
<!DOCTYPE html>
<html lang="en">
<head>
<meta charset="UTF-8">
<title>P&amp;W Realty Services – Open House Flyer</title>
<link rel="stylesheet" href="https://fonts.googleapis.com/css2?family=Montserrat:wght@700;800&family=Cinzel:wght@700&family=Tinos:wght@400;700&display=swap">
<style>
  :root {
    --navy: #1e2457;
    --gold: #f5a800;
    --lavender: #dcdce9;
    --stage: #d3d3d3;
    --ink: #1b1b2e;
    --muted: #3a3a4a;
    --white: #ffffff;
  }
  * { box-sizing: border-box; margin: 0; padding: 0; }
  html, body {
    width: 1200px; height: 741px; overflow: hidden;
    background: var(--stage);
  }
  .flyer {
    position: absolute; left: 330px; top: 21px;
    width: 540px; height: 698px;
    background: var(--lavender);
    overflow: hidden;
    font-family: "Tinos", "Times New Roman", serif;
  }
  .hero {
    position: absolute; left: 0; top: 0; width: 540px; height: 303px;
    background: linear-gradient(180deg, #6f9fd6 0%, #a9c3df 22%, #b7c8da 40%, #9fb2c6 62%, #8c8a78 82%, #6e6250 100%);
  }
  .hero-shapes { position: absolute; left: 0; top: 0; width: 540px; height: 303px; }
  .brand {
    position: absolute; left: 10px; top: 9px;
    display: flex; align-items: center; gap: 6px;
    font-family: "Tinos", "Times New Roman", serif; font-weight: 400;
    font-size: 14px; line-height: 16px; color: var(--navy);
  }
  .brand-mark { width: 8px; height: 8px; background: var(--navy); }
  .event-card {
    position: absolute; left: 29px; top: 230px; width: 221px; height: 265px;
    background: var(--navy); color: var(--white);
    padding: 32px 10px 0 10px;
  }
  .event-title {
    font-family: "Montserrat", Arial, sans-serif; font-weight: 800;
    font-size: 44px; line-height: 42px; text-align: center; letter-spacing: -0.5px;
  }
  .event-rule {
    width: 168px; height: 4px; background: var(--gold); margin: 8px auto 22px;
  }
  .event-details { font-size: 11.5px; line-height: 17px; }
  .features {
    position: absolute; left: 252px; top: 263px; width: 252px; height: 359px;
    background: var(--gold); color: var(--ink);
    padding: 0 10px;
  }
  .features-kicker {
    color: var(--navy);
    font-family: "Montserrat", Arial, sans-serif; font-weight: 700;
    font-size: 15px; margin: 0 -10px; padding: 0 10px 0 6px; height: 21px; line-height: 20px;
    border-bottom: 1px solid var(--navy);
    white-space: nowrap;
  }
  .features-title {
    font-family: "Cinzel", serif; font-weight: 700;
    font-size: 16px; letter-spacing: 1.5px; color: var(--navy);
    margin: 16px 0 10px 6px;
  }
  .feature-list { list-style: none; font-size: 13.5px; line-height: 19px; }
  .feature-list li { position: relative; padding-left: 9px; margin-bottom: 12px; }
  .feature-list li::before {
    content: ""; position: absolute; left: 0; top: 7px;
    width: 5px; height: 5px; border-radius: 50%; background: var(--ink);
  }
  .thumb { position: absolute; top: 502px; height: 91px; }
  .thumb-exterior { left: 29px; width: 134px; background: linear-gradient(180deg, #8fb1d8 0%, #9cb0c4 50%, #6d6a5c 100%); }
  .thumb-interior { left: 172px; width: 136px; background: linear-gradient(90deg, #5a3a22 0%, #c9b79a 45%, #efe7da 70%, #8a5a34 100%); }
  .thumb-deck { left: 317px; width: 173px; background: linear-gradient(180deg, #b9d0e6 0%, #c5ccd3 45%, #8b7a63 80%, #6b5a45 100%); }
  .contact {
    position: absolute; left: 0; top: 598px; width: 185px;
    text-align: right; font-size: 10px; line-height: 12.5px; color: var(--muted);
  }
  .contact-title {
    font-family: "Cinzel", serif; font-weight: 700; font-size: 14px;
    letter-spacing: 1.5px; color: var(--navy); line-height: 16px;
  }
  .contact-name { color: var(--gold); }
  .agent-photo {
    position: absolute; left: 196px; top: 598px; width: 54px; height: 91px;
    background: linear-gradient(180deg, #cfcfd2 0%, #a9a9ad 100%);
    border: 2px solid var(--white);
  }
</style>
</head>
<body>
  <main class="flyer">
    <div class="hero" role="img" aria-label="Photo of the two-storey colonial home exterior under a blue sky"></div>
    <svg class="hero-shapes" viewBox="0 0 540 303" aria-hidden="true">
      <polygon points="0,0 262,0 0,132" fill="#f5a800" opacity="0.88"/>
      <polygon points="0,0 120,0 0,58" fill="#1e2457" opacity="0.35"/>
      <polygon points="540,150 540,303 405,303" fill="#1e2457" opacity="0.9"/>
    </svg>
    <div class="brand"><span class="brand-mark"></span>P&amp;W Realty Services, LLC</div>

    <section class="features">
      <div class="features-kicker">BEST LOCATION PROPERTY</div>
      <h2 class="features-title">Property Features:</h2>
      <ul class="feature-list">
        <li>8 Room, 2.5 Bath Colonial style home</li>
        <li>Open concept, Kitchen, Dining room and Living room.</li>
        <li>Deck</li>
        <li>2 Car Garage</li>
      </ul>
    </section>

    <section class="event-card">
      <h1 class="event-title">OPEN<br>HOUSE</h1>
      <div class="event-rule"></div>
      <p class="event-details">
        Date of event: Saturday, July 18, 2020<br>
        Time of event 12-3<br>
        Location 48 Orchard Ln Hamden, CT<br>
        Listing price 249,999
      </p>
    </section>

    <div class="thumb thumb-exterior" role="img" aria-label="Photo of the house exterior from the side"></div>
    <div class="thumb thumb-interior" role="img" aria-label="Photo of the open-concept interior with stairs"></div>
    <div class="thumb thumb-deck" role="img" aria-label="Photo of the rear deck and yard"></div>

    <section class="contact">
      <div class="contact-title">CONTACT:</div>
      <div>P&amp;W Realty Services, LLC</div>
      <div class="contact-name">Marta Quinlan</div>
      <div>203 555-0187</div>
      <div>FB: P&amp;W Realty Service, LLC</div>
      <div>www.martaquinlan.net</div>
    </section>
    <div class="agent-photo" role="img" aria-label="Agent portrait placeholder"></div>
  </main>
</body>
</html>
```